Product label and brand logo for Superfood powder

We need a product label (incl. logo) for a new plant-based Superfood powder called "MyLumaRoot Health & Wellness Protein" ("MyLumaRoot" being the brand). The powder formula is comprised of various Superfoods that each offer a unique benefit to the customer. On top of that the formular includes real coffee for excellent taste. This is a premium product and some ingredients even come from organic sources. I've included an extended briefing with examples as a PDF. The final design should communicate wellbeing, health, wellness rather than target the sport and fitness crowd (as most protein powders do).
Target Market(s)
Health & Wellness Space
Industry/Entity Type
Health And Wellness
Requirements
Must have
- Please see attached PDF.
Nice to have

```html
<!DOCTYPE html>
<html lang="de">
<head>
<meta charset="utf-8">
<title>MyLumaRoot Health &amp; Wellness Protein – Etikett</title>
<link rel="stylesheet" href="https://fonts.googleapis.com/css2?family=Roboto:wght@300;400;500;700&family=Oswald:wght@500&family=Roboto+Condensed:wght@700&display=swap">
<style>
  :root{
    --bg:#8d8a89;
    --brown:#3f1e15;
    --maroon:#6b2a1c;
    --green:#6f8f3a;
    --ink:#222;
    --ink-soft:#3a3a3a;
    --orange:#f6a33a;
    --gold:#f3b63a;
    --badge:#d6d6d6;
    --white:#ffffff;
  }
  *{box-sizing:border-box;margin:0;padding:0}
  html,body{width:1200px;height:900px;overflow:hidden}
  body{background:var(--bg);font-family:"Roboto",Arial,sans-serif;color:var(--ink);position:relative}
  .label{position:absolute;left:50px;top:247px;width:1100px;height:406px;background:var(--white);overflow:hidden;box-shadow:0 6px 18px rgba(0,0,0,.25)}
  .label__bg{position:absolute;inset:0}
  .panel{position:absolute;top:0;height:100%}
  .panel--left{left:0;width:382px}
  .panel--front{left:382px;width:336px;text-align:center}
  .panel--right{left:718px;width:382px}

  .info{position:absolute;left:26px;width:254px;font-size:12px;line-height:14.5px;color:var(--ink)}
  .info strong{color:var(--maroon);font-weight:500}
  .info--ingredients{top:30px;text-align:justify}
  .info--amount{top:89px;color:var(--maroon)}
  .info--usage{top:123px}
  .info--distributor{top:177px}
  .origin-badge{position:absolute;left:26px;top:236px;width:94px;height:30px;border-radius:15px;background:var(--badge)}
  .best-before{position:absolute;left:26px;top:360px;font-size:12px;line-height:15px;color:var(--gold)}
  .best-before span{color:var(--white)}

  .brand{position:absolute;top:38px;left:0;width:100%;display:flex;justify-content:center;align-items:center;gap:8px}
  .brand__name{font-weight:400;font-size:30px;line-height:34px;color:var(--ink-soft)}
  .brand__dot{width:14px;height:14px;border-radius:50%;background:var(--green)}
  .headline{position:absolute;top:114px;width:100%;font-family:"Oswald",sans-serif;font-weight:500;font-size:29px;line-height:34px;color:var(--green);letter-spacing:1px}
  .product{position:absolute;top:144px;width:100%;font-family:"Roboto Condensed",sans-serif;font-weight:700;font-size:38px;line-height:42px;letter-spacing:14px;padding-left:14px;color:var(--ink)}
  .flavour{position:absolute;top:196px;width:100%;font-size:14px;color:var(--ink-soft)}
  .fact{position:absolute;top:236px;width:62px;height:62px;border-radius:50%;background:#1f1715;border:3px solid #d9d9d9;box-shadow:0 0 0 2px #3a2a25;color:var(--white);font-size:13px;line-height:14px;display:flex;flex-direction:column;justify-content:center}
  .fact--protein{left:37px}.fact--bcaa{left:137px}.fact--glutamin{left:236px}
  .cup{position:absolute;left:44px;top:322px;width:80px;height:64px;border-radius:8px;background:radial-gradient(circle at 50% 45%,#d9a36a,#7a4a2a 55%,#3a1f14)}
  .cup__seal{position:absolute;left:58px;top:340px;width:28px;height:28px;border-radius:50%;background:#5d8a2e;border:2px solid #e8e8e8}
  .banner{position:absolute;left:122px;top:322px}
  .banner__text{position:absolute;left:126px;top:332px;width:166px;color:var(--brown);text-align:center}
  .banner__main{font-size:13px;line-height:15px;letter-spacing:.3px}
  .banner__sub{font-size:7px;font-weight:700;margin-top:3px}
  .banner__free{font-size:9.5px;color:var(--white);margin-top:4px;word-spacing:6px}
  .net{position:absolute;top:393px;width:100%;font-size:7.5px;color:var(--white)}

  .sub-brand{position:absolute;left:101px;top:24px;font-size:10px;color:var(--maroon)}
  .sub-flavour{position:absolute;left:101px;top:37px;font-size:10px;font-weight:700;letter-spacing:3px;color:var(--maroon)}
  .nutrition{position:absolute;left:101px;top:54px;width:252px;border-collapse:collapse;font-size:8.5px}
  .nutrition th{background:var(--maroon);color:var(--white);font-weight:400;font-size:11px;text-align:left;padding:0 0 0 28px;height:25px;border:1px solid var(--maroon)}
  .nutrition td{height:18px;white-space:nowrap;border:1px solid #555;border-left:none;border-right:none;padding:0 3px}
  .nutrition tr td:first-child{border-left:1px solid #555;padding-left:11px;width:138px}
  .nutrition tr td:last-child{border-right:1px solid #555;text-align:right;padding-right:10px}
  .contact{position:absolute;left:101px;top:329px;list-style:none;font-size:12px;color:var(--white)}
  .contact li{display:flex;align-items:center;gap:6px;height:19px}
  .contact svg{flex:none}
</style>
</head>
<body>
<section class="label" aria-label="Produktetikett MyLumaRoot Health &amp; Wellness Protein">
  <svg class="label__bg" width="1100" height="406" viewBox="0 0 1100 406">
    <defs>
      <linearGradient id="front-sheen" x1="0" x2="1">
        <stop offset="0" stop-color="#e9e9e9"/><stop offset=".5" stop-color="#ffffff"/><stop offset="1" stop-color="#e6e6e6"/>
      </linearGradient>
      <linearGradient id="brown-fill" x1="0" y1="0" x2="0" y2="1">
        <stop offset="0" stop-color="#4a2519"/><stop offset="1" stop-color="#2e140d"/>
      </linearGradient>
    </defs>
    <rect x="382" y="0" width="336" height="406" fill="url(#front-sheen)"/>
    <rect x="0" y="0" width="1100" height="10" fill="var(--brown)"/>
    <path d="M0 284 Q550 206 1100 284" fill="none" stroke="#b9b9b9" stroke-width="4"/>
    <path d="M0 292 Q550 214 1100 292 L1100 406 L0 406 Z" fill="url(#brown-fill)"/>
    <path d="M0 290 Q550 212 1100 290" fill="none" stroke="#e2e2e2" stroke-width="2"/>
  </svg>

  <div class="panel panel--left">
    <p class="info info--ingredients"><strong>Zutaten:</strong> [Zutatenliste] Lorem Ipsum, Dummy text, Placed, As text, Lorem Ipsum, Dummy text, Placed, As text.</p>
    <p class="info info--amount">e 1.000 g / 25 Portionen</p>
    <p class="info info--usage"><strong>Verzehrempfehlung:</strong> 40 g Pulver im Shaker mit 400-500 ml Wasser mischen und gut schütteln.</p>
    <p class="info info--distributor"><strong>Vertrieb/Distributor:</strong><br>MyLumaRoot OG, Lindenweg 12,<br>8010 Graz, Österreich</p>
    <span class="origin-badge" role="img" aria-label="Herkunftssiegel"></span>
    <p class="best-before">Mindestens haltbar bis<br>Ende und Chargennummer: <span>siehe Boden</span></p>
  </div>

  <div class="panel panel--front">
    <div class="brand">
      <p class="brand__name">MyLumaRoot</p>
      <span class="brand__dot"></span>
    </div>
    <p class="headline">HEALTH &amp; WELLNESS</p>
    <p class="product">PROTEIN</p>
    <p class="flavour">Kaffeegeschmack</p>
    <div class="fact fact--protein">20 g<span>Protein</span></div>
    <div class="fact fact--bcaa">4 g<span>BCAA</span></div>
    <div class="fact fact--glutamin">4 g<span>Glutamin</span></div>
    <svg class="banner" width="196" height="64" viewBox="0 0 196 64">
      <path d="M0 6 L196 6 L172 32 L196 58 L0 58 Z" fill="#c8c8c8"/>
      <path d="M4 10 L184 10 L164 32 L184 54 L4 54 Z" fill="var(--orange)"/>
    </svg>
    <div class="cup" role="img" aria-label="Foto einer Tasse Kaffee mit Kaffeebohnen"></div>
    <span class="cup__seal" role="img" aria-label="Vegan-Siegel"></span>
    <div class="banner__text">
      <p class="banner__main">MIT ECHTEM KAFFEE</p>
      <p class="banner__sub">+ VITAMINE &nbsp; + MINERALSTOFFE</p>
      <p class="banner__free">Laktosefrei Glutenfree</p>
    </div>
    <p class="net">e 1.000 g / 25 Portionen</p>
  </div>

  <div class="panel panel--right">
    <p class="sub-brand">Health &amp; Wellness Protein</p>
    <p class="sub-flavour">Kaffeegeschmack</p>
    <table class="nutrition">
      <tr><th colspan="3">NUTRITIONAL VALUE</th></tr>
      <tr><td>Nährwerte</td><td>Pro 100 G</td><td>Pro 30 G</td></tr>
      <tr><td>Brennwert</td><td>479 kJ</td><td>479 kJ</td></tr>
      <tr><td>Brennwert</td><td>1597 kcal</td><td>113 kcal</td></tr>
      <tr><td>Fett</td><td>5.5 g</td><td>1.6 g</td></tr>
      <tr><td>Davon gesättigte Fettsäuren</td><td>1.8 g</td><td>0.56 g</td></tr>
      <tr><td>Kohlenhydrate</td><td>3 g</td><td>0.92 g</td></tr>
      <tr><td>davon Zucker</td><td>0 g</td><td>0 g</td></tr>
      <tr><td>Ballaststoffe</td><td>7.2 g</td><td>2.1 g</td></tr>
      <tr><td>Eiweiß</td><td>75.2 g</td><td>22.5 g</td></tr>
      <tr><td>Salz*</td><td>0.91 g</td><td>0.27 g</td></tr>
    </table>
    <ul class="contact">
      <li><svg width="14" height="14" viewBox="0 0 14 14"><circle cx="7" cy="7" r="7" fill="#fff"/><path d="M4.2 3.5 L5.6 3.3 L6.3 5.2 L5.4 6 Q6.2 7.7 7.9 8.6 L8.7 7.7 L10.6 8.4 L10.4 9.8 Q7 10.4 4.2 3.5Z" fill="var(--brown)"/></svg>+43 720 555 0142</li>
      <li><svg width="14" height="14" viewBox="0 0 14 14"><circle cx="7" cy="7" r="6" fill="none" stroke="#fff" stroke-width="1.3"/><path d="M1 7 H13 M7 1 Q3 7 7 13 M7 1 Q11 7 7 13" fill="none" stroke="#fff" stroke-width="1"/></svg>www.mylumaroot.net</li>
      <li><svg width="14" height="14" viewBox="0 0 14 14"><circle cx="7" cy="7" r="6.5" fill="#fff"/></svg>social: @mylumaroot</li>
    </ul>
  </div>
</section>
</body>
</html>
```